We need a Glass-Shattering Brochure

We area start up renewable company based in the UK but operate in West Africa. We have a unique blend of local know-how and international exposure to latest solar technology. We pride ourselves in bringing next generation, ground breaking, value for money solar products to Africa.

We are launching a massive campaign to introduce some of the world's best solar product to our high net-worth clients and decision makers. This will be a single brochure of A4 size on 8 pages. Details of the page content is attached.

Also a sample of what we like is attached. The brochure must be clean , fresh, very contemporary and straight to the point - Clear

I have attached a link to some of our installation pictures and some pictures that I think you might need. But feel free to source pictures you think will be appropriate for the intended audience.

You can access some of our paid pictures and installation pictures here https://filedrop-example.net/f/x7KpQm2RtLw9ZvNc4HdYs8BjE

Apologies to everyone. We have just uploaded the brochure content

Target Market(s)

Top company executives

Industry/Entity Type

It Company

Requirements
Must have
• Similar font used in the sample brochure attached. White background. Hint of the green. Please check out our website at www.tolvarpower.co.uk
Nice to have
• Other pictures other than the ones provided

```html
<!DOCTYPE html>
<html lang="en">
<head>
<meta charset="utf-8">
<title>Tolvar Power Brochure Spread</title>
<link rel="stylesheet" href="https://fonts.googleapis.com/css2?family=Didact+Gothic&family=Questrial&display=swap">
<style>
  :root {
    --bg: #e4e6e8;
    --sky-deep: #2c66b3;
    --sky-mid: #4d89cf;
    --sky-light: #8dbbe6;
    --page-pale: #dce9f6;
    --page-white: #f4f8fc;
    --green-dark: #2f7a3a;
    --green-mid: #4f9a2f;
    --green-lime: #8cc43c;
    --green-pale: #b9de6a;
    --navy: #1f3f7a;
    --text-white: #ffffff;
    --photo-roof-a: #6d8fb8;
    --photo-roof-b: #8a9a7a;
    --photo-array-a: #9fc3e6;
    --photo-array-b: #3c4656;
    --photo-house-a: #7fae5e;
    --photo-house-b: #c9b58e;
  }
  * { box-sizing: border-box; margin: 0; padding: 0; }
  html, body { width: 1200px; height: 789px; overflow: hidden; background: var(--bg); }
  body { font-family: "Didact Gothic", "Questrial", sans-serif; }

  .spread {
    position: absolute; left: 50px; top: 6px;
    width: 1100px; height: 777px;
    display: flex;
    box-shadow: 0 6px 18px rgba(0,0,0,.25);
  }
  .page { position: relative; width: 550px; height: 777px; overflow: hidden; }
  .page--left { background: linear-gradient(180deg, var(--sky-deep) 0%, var(--sky-mid) 35%, var(--sky-light) 55%, #cfe2f3 70%); }
  .page--right { background: linear-gradient(180deg, #a9c9ea 0%, var(--page-pale) 30%, var(--page-white) 60%); }
  .spine {
    position: absolute; left: 535px; top: 0; width: 30px; height: 777px;
    background: linear-gradient(90deg, rgba(0,0,0,0) 0%, rgba(0,0,0,.18) 50%, rgba(0,0,0,0) 100%);
    pointer-events: none; z-index: 6;
  }

  .page svg.shapes { position: absolute; inset: 0; width: 100%; height: 100%; z-index: 2; }

  .section-title {
    position: absolute; top: 26px; left: 22px;
    color: var(--text-white); font-family: "Questrial", sans-serif;
    font-size: 17px; letter-spacing: .5px; z-index: 3;
  }

  .copy { position: absolute; z-index: 3; font-size: 11.2px; line-height: 1.32; }
  .copy p + p { margin-top: 9px; }
  .page--left .copy { left: 24px; top: 112px; width: 480px; color: var(--text-white); }
  .page--right .copy { left: 24px; top: 122px; width: 490px; color: var(--navy); }

  .copy .lead-out { font-size: 13.5px; line-height: 1.3; font-weight: 700; margin-top: 12px; }
  .copy .call-out { color: var(--green-mid); font-size: 13px; font-weight: 700; margin-top: 14px; }

  .photo { position: absolute; z-index: 1; }
  .photo--rooftops { left: 0; top: 392px; width: 550px; height: 300px;
    background: linear-gradient(170deg, #a7c7e6 0%, var(--photo-roof-b) 25%, var(--photo-roof-a) 55%, #c9ced4 100%); }
  .photo--array { left: 0; top: 430px; width: 550px; height: 260px;
    background: linear-gradient(160deg, var(--photo-array-a) 0%, #b8cfe3 30%, var(--photo-array-b) 60%, #8a8f7c 100%); }
  .photo--house {
    position: absolute; z-index: 4; border-radius: 50%;
    border: 4px solid var(--green-lime);
  }
  .photo--house-small { left: 130px; top: 610px; width: 90px; height: 90px;
    background: radial-gradient(circle at 50% 40%, #e8e4d6 0%, var(--photo-house-b) 45%, var(--photo-house-a) 100%); }
  .photo--house-large { left: 212px; top: 584px; width: 130px; height: 130px;
    background: radial-gradient(circle at 50% 35%, #e9d7a6 0%, var(--photo-house-b) 40%, var(--photo-house-a) 75%, #4f8c3e 100%); }

  .web-address {
    position: absolute; left: 26px; bottom: 36px; z-index: 4;
    display: flex; align-items: center; gap: 10px;
    color: var(--text-white); font-size: 15px; letter-spacing: .3px;
  }
  .web-address svg { width: 14px; height: 14px; }
</style>
</head>
<body>
<div class="spread">

  <section class="page page--left">
    <div class="photo photo--rooftops" role="img" aria-label="Photograph of large rooftops covered with solar panels beside green hills"></div>

    <svg class="shapes" viewBox="0 0 550 777" preserveAspectRatio="none" aria-hidden="true">
      <path d="M0 18 H360 L372 52 H0 Z" fill="var(--green-dark)"/>
      <path d="M0 52 H372 C430 52 470 70 550 100 V118 C470 88 420 64 360 60 H0 Z" fill="var(--green-lime)"/>
      <path d="M360 18 C430 26 490 52 550 84 V100 C470 70 430 52 372 52 Z" fill="var(--green-pale)"/>
      <path d="M0 640 C150 600 330 610 550 680 V777 H0 Z" fill="var(--green-dark)"/>
      <path d="M0 610 C150 575 330 590 550 660 V674 C330 606 150 594 0 628 Z" fill="var(--green-lime)"/>
      <path d="M0 628 C150 594 330 606 550 674 V680 C330 612 150 600 0 636 Z" fill="#ffffff"/>
    </svg>

    <h2 class="section-title">DIASPORA</h2>

    <div class="copy">
      <p>Millions of people are migrating to Africa, to join of the great emergence of some of the fastest growing economies in the world. We want to make sure your relocation is enhanced by providing the option of constant power supply from our solar system. This product is focused on meeting your needs right before you arrive in Africa. If you are relocating to Africa, building/buying a holiday home, setting up a small business or buying for mum's house or dad's mansion, we want to make 24 hour power access a reality.</p>
      <p>We promise you will get the same quality of delivery you might expect to get anywhere in the world with some of the quality names you are familiar with. We will give you that top notch service that exceeds your expectation.</p>
      <p>Imagine the benefit of not worrying about getting petrol, diesel for that generator or the noise and fumes it will produce at night or if there will be power from the grid to run the pumping machine.</p>
      <p class="lead-out">This is the ultimate level of luxury you deserve. If you are moving back to Africa or what to buy for a family member. Contact us, tell us where you are, what you need, and when you need it. Drop us a message on Linkly</p>
    </div>

    <div class="web-address">
      <svg viewBox="0 0 14 14" aria-hidden="true"><circle cx="7" cy="7" r="6" fill="none" stroke="#fff" stroke-width="1.2"/><path d="M1 7 H13 M7 1 C4 4 4 10 7 13 M7 1 C10 4 10 10 7 13" fill="none" stroke="#fff" stroke-width="1"/></svg>
      <span>www.tolvarpower.co.uk</span>
    </div>
  </section>

  <section class="page page--right">
    <div class="photo photo--array" role="img" aria-label="Photograph of ground-mounted solar panel arrays under a clear sky"></div>

    <svg class="shapes" viewBox="0 0 550 777" preserveAspectRatio="none" aria-hidden="true">
      <path d="M0 18 H380 L392 52 H0 Z" fill="var(--green-lime)"/>
      <path d="M0 52 H392 C440 52 480 66 550 94 V112 C480 84 440 62 380 60 H0 Z" fill="var(--green-mid)"/>
      <path d="M380 18 C440 24 500 48 550 76 V94 C480 66 440 52 392 52 Z" fill="var(--green-pale)"/>
      <path d="M0 700 C170 680 360 660 550 600 V777 H0 Z" fill="var(--green-dark)"/>
      <path d="M0 680 C170 660 360 640 550 580 V596 C360 656 170 676 0 694 Z" fill="var(--green-lime)"/>
      <path d="M0 694 C170 676 360 656 550 596 V602 C360 662 170 682 0 702 Z" fill="#ffffff"/>
    </svg>

    <h2 class="section-title">SME</h2>

    <div class="copy">
      <p>Small-Scale Medium Enterprises are the backbone of the African economy providing 80% of its employment workforce. These SME often struggle to provide sustainable business model with the increasing energy crisis. In other words Africa's economy is totally backed by generators. However current dependency on generators is proving more costly and detrimental to the environment. But with today's advancement in solar technology, we are reversing the conversation from a generator backed economy to solar powered economy.</p>
      <p>Tolvar Power has initiated a new product called Sun Step Plan to help SMEs and small businesses get on the ladder of power independence. The product will offer a manageable Pay Us You Go for solar systems from 5kVa to 25kVa. SMEs will have the benefit of having power generation for 24hrs at a cheaper rate than current diesel generators and conventional grid.</p>
      <p>We want to hear from you if you are Small-Scale Medium Enterprise operating anywhere in Africa. If you are a bakery owner, poultry farmer, cold room store operative. If you consider your business as a small business, and you want to stop using the noisy, erratic generator. If you want to have access to electricity round the clock 365 days at a cheaper rate, we want to support that vision.</p>
      <p class="call-out">If you need a solar plant for your business from 5kva to 350kva and you want a pay as you go option, contact us now.</p>
    </div>

    <div class="photo--house photo--house-small" role="img" aria-label="Photograph of a modern white house"></div>
    <div class="photo--house photo--house-large" role="img" aria-label="Photograph of a large villa with solar panels on the roof and a green lawn"></div>
  </section>

  <div class="spine" aria-hidden="true"></div>
</div>
</body>
</html>
```